I am seeking someone to design a placemat for our leadership team, that includes the key concepts from our work with a leadership consultant. The place mate should incorporate all of the information from the 'Leadership Placemat' document. The document contains a range of diagrams and models that i would like modified and made consistent for this placemat.

I'm wanting the placemat to be a single side A3 page, that includes some design work to make each of the concepts have a consistent visual look.

My preference would be a design that incorporates modified versions of all of the diagrams and concepts to look either highly professional in layout, look and feel.

```html
<!DOCTYPE html>
<html lang="en">
<head>
<meta charset="utf-8">
<title>Leadership Placemat 2023</title>
<link href="https://fonts.googleapis.com/css2?family=League+Spartan:wght@700;800&family=Nunito:wght@700;800&family=Roboto+Condensed:wght@400;700&family=Montserrat:wght@400;600&display=swap" rel="stylesheet">
<style>
:root{
  --teal:#4fb3a9;
  --navy:#17415a;
  --ink:#1c1c1c;
  --pink:#ef3f5e;
  --orange:#f7a93b;
  --coral:#f26b4f;
  --blue:#1f6fb0;
  --sky:#7fd0e6;
  --col-a:#dfe5ea;
  --col-b:#c8d2d9;
  --text:#2a3640;
  --heading:#1d4d66;
}
*{box-sizing:border-box;margin:0;padding:0}
html,body{width:1200px;height:943px;overflow:hidden;background:#fff}
body{font-family:"Roboto Condensed",sans-serif;color:var(--text)}
.placemat{position:relative;width:1200px;height:943px;background:#fff}
.title{position:absolute;top:42px;left:0;width:1200px;text-align:center;font-family:"League Spartan",sans-serif;font-weight:800;font-size:64px;letter-spacing:1px;line-height:1}
.title .t1{color:var(--teal)}
.title .t2{color:var(--ink)}
.title .t3{color:var(--pink)}
.columns{position:absolute;top:128px;left:50px;width:1100px;height:760px;display:flex}
.column{width:220px;height:100%;display:flex;flex-direction:column;overflow:hidden}
.column:first-child .col-head{border-top-left-radius:14px}
.column:last-child .col-head{border-top-right-radius:14px}
.col-head{height:54px;background:var(--navy);color:#fff;font-family:"Nunito",sans-serif;font-weight:800;font-size:20px;display:flex;align-items:center;justify-content:center;letter-spacing:.5px;flex:none}
.col-body{flex:1;padding:7px 9px;background:var(--col-a);border-radius:0 0 10px 10px;overflow:hidden;position:relative}
.column.alt .col-body{background:var(--col-b)}
h3{font-family:"Nunito",sans-serif;font-weight:800;color:var(--heading);font-size:13.5px;line-height:1.1;margin:4px 0 3px}
p,li{font-size:6.6px;line-height:1.35}
.lead{font-size:10px;line-height:1.2;color:#222}
.sans{font-family:"Montserrat",sans-serif}
.row{display:flex;gap:6px;align-items:flex-start}
ul.dots{list-style:none}
ul.dots li{position:relative;padding-left:9px;margin-bottom:1px}
ul.dots li::before{content:"";position:absolute;left:1px;top:2.5px;width:4px;height:4px;border-radius:50%;background:var(--pink)}
ul.ticks{list-style:none}
ul.ticks li{position:relative;padding-left:9px;margin-bottom:1px}
ul.ticks li::before{content:"";position:absolute;left:0;top:1.5px;width:4.5px;height:4.5px;border:1px solid var(--pink);border-radius:1px}
.placeholder{border-radius:3px}
/* purpose */
.golden h4{font-family:"Nunito",sans-serif;font-size:8px;color:var(--navy);margin-top:1px}
.concept-band{background:#2c2f33;color:#fff;font-family:"Nunito",sans-serif;font-weight:800;font-size:10.5px;line-height:1.2;margin:6px -9px 6px;padding:5px 9px}
.hpc{display:flex;align-items:center;gap:4px;font-size:7.5px}
.hpc-label{font-weight:700;font-size:7.5px;color:#222;width:44px;line-height:1.2}
.hpc-items p{font-family:"Montserrat",sans-serif;font-size:6.8px;line-height:1.2;margin:5px 0}
.book{height:200px;background:linear-gradient(#f6f6f6,#e2e4e6);border:1px solid #cfd4d8;margin:3px 0 8px}
ol.numbered{padding-left:12px}
ol.numbered li{font-family:"Montserrat",sans-serif;font-size:7px;margin-bottom:6px;line-height:1.25}
/* leadership */
table.levels{width:100%;border-collapse:separate;border-spacing:0 2px;margin:3px 0}
table.levels td{font-size:6px;padding:1px 4px;height:10px}
table.levels td:first-child{background:#fff;border:1px solid #8a98a3;width:42%}
table.levels td:last-child{background:var(--navy);color:#fff}
.ladder-img{width:92px;height:66px;background:linear-gradient(135deg,#ffffff,#eceff1);border:1px solid #d3d8dc;flex:none}
.check-grid{display:grid;grid-template-columns:1fr 1.3fr;column-gap:4px}
/* feedback */
.icons-row{display:flex;justify-content:space-between;padding:0 4px;margin:6px 0 2px}
.icons-row div{text-align:center;font-size:9px;color:#222}
.small-head{font-weight:700;font-size:6.6px;margin:4px 0 3px;color:#222}
/* term */
.eq{display:flex;align-items:center;gap:3px;margin:5px 0 6px;font-size:11px;font-weight:700;color:#222}
.eq .n{width:18px;height:18px;border-radius:50%;display:flex;align-items:center;justify-content:center;font-size:9.5px;color:#222;border:2px solid #fff;box-shadow:0 0 0 1px rgba(0,0,0,.08)}
.n.t{background:var(--teal)}.n.r{background:var(--coral)}.n.o{background:var(--orange)}
.life{position:absolute;left:0;right:0;bottom:76px;background:#fff;border-radius:12px;overflow:hidden}
.life-top{background:var(--navy);color:#fff;padding:10px 14px 9px}
.life-top h4{font-family:"Nunito",sans-serif;font-size:13px}
.life-top p{font-size:8.5px;font-weight:700;margin-top:3px}
.life-bottom{padding:8px 4px 6px;text-align:center}
.life-bottom h5{font-family:"Montserrat",sans-serif;color:var(--teal);font-size:8px;letter-spacing:.8px;line-height:1.2;font-weight:600}
</style>
</head>
<body>
<main class="placemat">
  <h1 class="title"><span class="t1">LEADERSHIP</span> <span class="t2">PLACEMAT -</span> <span class="t3">2023</span></h1>

  <div class="columns">
    <!-- PURPOSE -->
    <section class="column">
      <div class="col-head">PURPOSE</div>
      <div class="col-body">
        <div class="row golden">
          <svg width="66" height="70" viewBox="0 0 66 70" aria-label="Why, how, what circles">
            <circle cx="33" cy="36" r="31" fill="var(--orange)"/>
            <circle cx="33" cy="32" r="23" fill="#fff"/>
            <circle cx="33" cy="27" r="13" fill="var(--pink)"/>
            <text x="33" y="29.5" font-size="6" fill="#fff" text-anchor="middle" font-weight="700">WHY</text>
            <text x="33" y="50" font-size="5.5" fill="#222" text-anchor="middle" font-weight="700">HOW</text>
            <text x="33" y="63" font-size="5.5" fill="#fff" text-anchor="middle" font-weight="700">WHAT</text>
          </svg>
          <div>
            <h4>What</h4>
            <p>Every organization on the planet knows WHAT they do. These are products they sell or the services they offer.</p>
            <h4>How</h4>
            <p>Some organizations know HOW they do it. These are the things that make them special or set them apart from their competition.</p>
          </div>
        </div>
        <div class="row" style="margin-top:3px">
          <h4 style="font-family:Nunito,sans-serif;font-size:8px;color:var(--navy)">Why</h4>
          <p>Very few organizations know WHY they do what they do. WHY is not about making money. That's a result. It's a purpose, cause or belief. It's the very reason your organization exists.</p>
        </div>
        <div class="concept-band">Key concepts of a performance, planning and development culture:</div>
        <div class="hpc">
          <div class="hpc-label">High Performance culture</div>
          <svg width="38" height="86" viewBox="0 0 38 86" aria-hidden="true">
            <path d="M6 6 Q20 0 30 10 L26 26 Q14 30 6 20 Z" fill="var(--pink)"/>
            <path d="M22 28 Q34 30 34 44 Q34 56 22 58 Q16 44 22 28 Z" fill="var(--orange)"/>
            <path d="M4 62 Q18 56 28 64 L24 80 Q12 84 4 74 Z" fill="#3aa0d6"/>
          </svg>
          <div class="hpc-items">
            <p>Purpose, Vision Strategy, Plan Align, and Act</p>
            <p style="margin:14px 0">Professional learning</p>
            <p>Accountability Anked to planning that uses feedback, coaching, reflection and review</p>
          </div>
        </div>
        <h3>The infinite game</h3>
        <div class="book placeholder" role="img" aria-label="Open book illustration with hand-lettered comparison of the finite game and the infinite game"></div>
        <ol class="numbered">
          <li>Live and lead to further a just cause</li>
          <li>Build trust in teams</li>
          <li>Find worthy rivals</li>
          <li>Display existential flexibility to make extreme strategic shifts</li>
          <li>Find the courage to lead with an infinite mindset</li>
        </ol>
      </div>
    </section>

    <!-- LEADERSHIP -->
    <section class="column alt">
      <div class="col-head">LEADERSHIP</div>
      <div class="col-body">
        <h3>Leading and Managing</h3>
        <p>Everyone needs to know when to lead and when to manage<br>Teachers need to be the leader of learning – in and out of the classroom!<br>When do you need to step in and manage, direct and/or take charge?</p>
        <svg width="200" height="58" viewBox="0 0 200 58" aria-label="Managing and leading balance">
          <circle cx="28" cy="32" r="16" fill="none" stroke="#7a5aa6" stroke-width="7"/>
          <path d="M28 16 A16 16 0 0 1 44 32" fill="none" stroke="#c8d34a" stroke-width="7"/>
          <polyline points="40,20 58,10 90,10" fill="none" stroke="var(--pink)" stroke-width=".8"/>
          <polyline points="40,42 58,48 90,48" fill="none" stroke="var(--pink)" stroke-width=".8"/>
          <text x="92" y="14" font-family="Nunito" font-weight="800" font-size="13" fill="var(--heading)">Managing</text>
          <text x="92" y="52" font-family="Nunito" font-weight="800" font-size="13" fill="var(--heading)">Leading</text>
        </svg>
        <h3>Levels of perspective</h3>
        <p>Perception is your reality. Understand how you and others make meaning.</p>
        <p>You keep your mental models if you are operating as mostly a manager.</p>
        <table class="levels">
          <tr><td>Purpose</td><td>Why?</td></tr>
          <tr><td>Vision</td><td>What you want to see</td></tr>
          <tr><td>Mental model</td><td>Values and beliefs</td></tr>
          <tr><td>Systemic structures</td><td>Systems and processes</td></tr>
          <tr><td>Patterns of behaviour</td><td>Habit and routines rituals and celebrations</td></tr>
          <tr><td>Events</td><td>Outcomes and outputs</td></tr>
        </table>
        <div class="row" style="align-items:center;gap:4px">
          <div style="width:72px;text-align:center;font-size:5.6px;line-height:1.6">Vision<br>Mental models<br>Systemic structure<br>Patterns of behaviour<br>Events</div>
          <svg width="34" height="60" viewBox="0 0 34 60" aria-label="Leverage arrow">
            <polygon points="17,2 32,20 23,20 23,58 11,58 11,20 2,20" fill="var(--navy)"/>
            <text x="17" y="38" fill="#fff" font-size="4" text-anchor="middle" transform="rotate(90 17 38)">LEVERAGE</text>
          </svg>
          <svg width="78" height="60" viewBox="0 0 78 60" aria-label="Balance of self belief and self awareness">
            <line x1="39" y1="4" x2="39" y2="50" stroke="var(--navy)" stroke-width="2"/>
            <line x1="12" y1="10" x2="66" y2="10" stroke="var(--navy)" stroke-width="1.5"/>
            <path d="M4 28 L12 12 L20 28 Z" fill="none" stroke="var(--navy)" stroke-width=".8"/>
            <path d="M58 28 L66 12 L74 28 Z" fill="none" stroke="var(--navy)" stroke-width=".8"/>
            <path d="M3 28 H21 Q12 34 3 28" fill="var(--navy)"/>
            <path d="M57 28 H75 Q66 34 57 28" fill="var(--navy)"/>
            <rect x="31" y="50" width="16" height="3" fill="var(--navy)"/>
            <text x="12" y="40" font-size="5.5" font-weight="700" text-anchor="middle" fill="#222">Self</text>
            <text x="12" y="46" font-size="5.5" font-weight="700" text-anchor="middle" fill="#222">Belief</text>
            <text x="66" y="40" font-size="5.5" font-weight="700" text-anchor="middle" fill="#222">Self</text>
            <text x="66" y="46" font-size="5.5" font-weight="700" text-anchor="middle" fill="#222">Awareness</text>
          </svg>
        </div>
        <h3>The Ladder of Inference</h3>
        <div class="row">
          <ul class="dots" style="flex:1">
            <li>You select different data depending on your mental model</li>
            <li>Reflexive loop should be a reflexive loop, or it is a delicious loop of self delusion</li>
            <li>You need to come back down the ladder.</li>
          </ul>
          <div class="ladder-img placeholder" role="img" aria-label="Ladder of inference illustration: situation, data, meaning, assumptions, conclusion, mental model, action"></div>
        </div>
        <svg width="200" height="100" viewBox="0 0 200 100" aria-label="The Pit chart">
          <text x="46" y="8" font-size="5" fill="var(--coral)">L+</text>
          <text x="40" y="98" font-size="5" fill="var(--coral)">L++</text>
          <line x1="56" y1="4" x2="56" y2="92" stroke="#333" stroke-width=".8"/>
          <line x1="56" y1="48" x2="196" y2="48" stroke="#333" stroke-width=".8"/>
          <polygon points="196,46 199,48 196,50" fill="#333"/>
          <path d="M56 48 C80 50 80 88 98 88 C120 88 140 40 170 6" fill="none" stroke="var(--pink)" stroke-width="1.2"/>
          <text x="4" y="26" font-size="5.5" fill="#333">clear understood</text>
          <text x="4" y="33" font-size="5.5" fill="#333">flows</text>
          <text x="4" y="66" font-size="5.5" fill="#333">confusion</text>
          <text x="4" y="73" font-size="5.5" fill="#333">frustration angst</text>
          <text x="98" y="68" font-size="9" fill="#222">The Pit</text>
          <text x="170" y="62" font-size="5.5" fill="#333">Time</text>
        </svg>
        <h3>Promote scholarly teaching</h3>
        <div class="check-grid">
          <ul class="ticks"><li>Teachers must be scholarly</li><li>Must consult the research</li><li>Scholarly</li><li>Consult literature.</li></ul>
          <ul class="ticks"><li>Select and apply appropriate interventions.</li><li>Conduct systematic observations.</li><li>Analyse outcomes</li><li>Obtain peer evaluation of their classroom performance</li></ul>
        </div>
        <p style="margin-top:4px">Scholarly teaching involves both informal and formal traditions. Research on teaching and learning and in-depth understanding of literature, critical reflection and sharing through publication.</p>
      </div>
    </section>

    <!-- FEEDBACK -->
    <section class="column">
      <div class="col-head">FEEDBACK</div>
      <div class="col-body">
        <h3>Model an effective feedback culture</h3>
        <p class="lead">All levels of feedback</p>
        <div class="icons-row">
          <div>
            <svg width="28" height="28" viewBox="0 0 28 28" aria-hidden="true"><g fill="none" stroke="var(--pink)" stroke-width="1.4"><rect x="2" y="2" width="10" height="10" rx="2"/><rect x="16" y="2" width="10" height="10" rx="2"/><rect x="2" y="16" width="10" height="10" rx="2"/><rect x="16" y="16" width="10" height="10" rx="2"/></g></svg>
            <br>Teams</div>
          <div>
            <svg width="34" height="28" viewBox="0 0 34 28" aria-hidden="true"><g fill="none" stroke="var(--navy)" stroke-width="1.4"><rect x="2" y="16" width="5" height="10"/><rect x="10" y="12" width="5" height="14"/><rect x="18" y="6" width="5" height="20"/><rect x="26" y="2" width="5" height="24"/></g></svg>
            <br>At level</div>
          <div>
            <svg width="34" height="28" viewBox="0 0 34 28" aria-hidden="true"><g fill="none" stroke="var(--orange)" stroke-width="1.3"><circle cx="8" cy="7" r="5"/><rect x="4" y="20" width="4" height="6"/><rect x="11" y="16" width="4" height="10"/><rect x="18" y="12" width="4" height="14"/><rect x="25" y="8" width="4" height="18"/><polyline points="14,10 30,2"/></g></svg>
            <br>Above level</div>
        </div>
        <p class="lead" style="margin:6px 0 4px">What will we - Start, stop, continue develop?</p>
        <h3>Deep listening</h3>
        <p class="lead">Am I:</p>
        <div class="check-grid" style="grid-template-columns:1fr 1fr;margin:3px 0 4px">
          <ul class="ticks"><li>Conversing or convincing?</li><li>Waiting to speak?</li></ul>
          <ul class="ticks"><li>Thinking what to say?</li><li>Evaluating what is being said?</li></ul>
        </div>
        <p class="lead">Skilled questions to ask:</p>
        <ul class="dots" style="margin:3px 0">
          <li>How long has this been an issue?</li>
          <li>What action have you taken?</li>
          <li>What is the outcome that you are looking for?</li>
          <li>What is the best way to move this forward?</li>
          <li>How would you like me to be involved here?</li>
        </ul>
        <p class="small-head">After deep listening, follow up questions may help:</p>
        <ul class="dots">
          <li>How will you know if you have reached a point where you are pleased with the situation?; describe what is happening.</li>
          <li>Who else do you need to consult, and what additional date do you need to gather?</li>
          <li>What decisions can you make now and action immediately?</li>
          <li>What do you really want?</li>
          <li>What are all the options available to you?</li>
          <li>What are the priorities for you?</li>
          <li>How would XXXX describe the situation?</li>
          <li>How do you think XXXX feels about the situation?</li>
          <li>What do you need to do differently to move this forward?</li>
        </ul>
        <p class="small-head" style="margin-top:6px">Check for understanding - foldback</p>
        <p>Don't presume it's a will issue!</p>
        <p class="small-head" style="margin-top:6px">WHY IS IT SOMEONE IS NOT DOING WHAT YOU EXPECT? WHY DO WE FIND IT SO HARD TO CHANGE OURSELVES? (TSAW Model)</p>
        <svg width="200" height="96" viewBox="0 0 200 96" aria-label="Skill, will, time and awareness model">
          <circle cx="100" cy="48" r="34" fill="var(--navy)"/>
          <text fill="#fff" font-size="5.6" text-anchor="middle"><tspan x="100" y="30">Our default</tspan><tspan x="100" y="37">is to often</tspan><tspan x="100" y="44">assume it is</tspan><tspan x="100" y="51">about Will</tspan><tspan x="100" y="58">Check the</tspan><tspan x="100" y="65">others.</tspan></text>
          <circle cx="74" cy="20" r="12" fill="#3aa0d6" stroke="#fff" stroke-width="2"/>
          <circle cx="128" cy="20" r="12" fill="var(--teal)" stroke="#fff" stroke-width="2"/>
          <circle cx="74" cy="76" r="12" fill="var(--orange)" stroke="#fff" stroke-width="2"/>
          <circle cx="128" cy="76" r="12" fill="var(--pink)" stroke="#fff" stroke-width="2"/>
          <text x="36" y="22" font-size="6" fill="#222">Skill</text>
          <text x="150" y="22" font-size="6" fill="#222">Will</text>
          <text x="36" y="78" font-size="6" fill="#222">Time</text>
          <text x="150" y="78" font-size="6" fill="#222">Awareness</text>
        </svg>
      </div>
    </section>

    <!-- CULTURE -->
    <section class="column alt">
      <div class="col-head">CULTURE</div>
      <div class="col-body">
        <h3>Culture and strategy</h3>
        <div class="row">
          <div class="placeholder" role="img" aria-label="Cartoon chick hatching from an egg" style="width:58px;height:70px;flex:none;background:radial-gradient(circle at 50% 45%,#f7c84a,#e9a56a 60%,#c8d2d9 72%)"></div>
          <div>
            <p>Culture doesn't eat strategy for breakfast<br>Culture needs to sit down with strategy for breakfast!</p>
            <p style="margin-top:6px">We need a culture where people can disagree without being disagreeable</p>
            <p style="margin-top:4px">Resisters are not bad people or enemies – enemies are people who are actively out to get you!</p>
          </div>
        </div>
        <p class="lead" style="text-align:center;margin:6px 0 2px">People to work with</p>
        <svg width="200" height="150" viewBox="0 0 200 150" aria-label="Venn diagram of dream big, get work done and know how to have fun">
          <circle cx="100" cy="108" r="38" fill="#f5e3bd"/>
          <circle cx="76" cy="64" r="40" fill="var(--pink)"/>
          <circle cx="124" cy="64" r="40" fill="#fff"/>
          <path d="M100 32.8 A40 40 0 0 1 100 95.2 A40 40 0 0 1 100 32.8Z" fill="#f27aa4"/>
          <path d="M64 102 A38 38 0 0 0 100 70 A40 40 0 0 0 70 103Z" fill="var(--coral)"/>
          <path d="M100 72 L112 94 Q100 100 88 94 Z" fill="var(--navy)"/>
          <text x="62" y="58" font-family="Nunito" font-weight="800" font-size="8.5" fill="#fff" text-anchor="middle">Dream Big</text>
          <text x="62" y="67" font-size="6.5" fill="#fff" text-anchor="middle">The wishbone</text>
          <text x="142" y="58" font-family="Nunito" font-weight="800" font-size="8.5" fill="var(--navy)" text-anchor="middle">Get work</text>
          <text x="142" y="66" font-family="Nunito" font-weight="800" font-size="8.5" fill="var(--navy)" text-anchor="middle">done</text>
          <text x="142" y="75" font-size="6.5" fill="var(--navy)" text-anchor="middle">The backbone</text>
          <text x="100" y="116" font-family="Nunito" font-weight="800" font-size="8" fill="var(--navy)" text-anchor="middle">Know how</text>
          <text x="100" y="124" font-family="Nunito" font-weight="800" font-size="8" fill="var(--navy)" text-anchor="middle">to have fun</text>
          <text x="100" y="132" font-size="6.3" fill="var(--navy)" text-anchor="middle">The funny bone</text>
        </svg>
        <p class="sans" style="font-size:7px;font-weight:600;margin:4px 0 10px">Chief Affirmation Officer</p>
        <h3>Self-worth</h3>
        <p class="sans" style="font-size:7px;margin:4px 0 8px">Find self-worth independent of what you do, or you will never be satisfied!</p>
        <p class="sans" style="font-size:7px;margin-bottom:8px">Don't get caught up in the narratives of others!</p>
        <p class="sans" style="font-size:7px;font-style:italic;margin-bottom:12px">I don't care about what you think about me, but I still care about you</p>
        <h3>Two expectations that kill performances</h3>
        <ul class="dots sans" style="margin:5px 0 10px">
          <li style="font-size:7px;margin-bottom:4px">Expectation of outcome</li>
          <li style="font-size:7px">Expectation of what people can't control</li>
        </ul>
        <p class="sans" style="font-size:8.5px;font-weight:600;color:#222">Focus on the things you can control.</p>
      </div>
    </section>

    <!-- TERM -->
    <section class="column">
      <div class="col-head">TERM</div>
      <div class="col-body">
        <h3>Supporting teams to thrive</h3>
        <div class="eq"><span class="n t">10</span>+<span class="n r">10</span>+<span class="n o">10</span>+<span class="n t">10</span>&nbsp;= 40</div>
        <div class="eq"><span class="n t">10</span>+<span class="n r">10</span>-<span class="n o">10</span>-<span class="n t">10</span>&nbsp;= 0</div>
        <div class="eq"><span class="n t">10</span>x<span class="n r">10</span>x<span class="n o">10</span>x<span class="n t">10</span>&nbsp;= 10,000</div>
        <div class="eq" style="align-items:flex-start"><span class="n t">8</span>x<span class="n r">8</span>x<span class="n o">8</span>x<span class="n t">8</span>&nbsp;<span style="line-height:1.1">= 2,401<br>= 4,096</span></div>
        <p style="margin-top:4px">We will work to ensure that we are seeing the multiplication effect with our teams. We'll be mindful of burnout and ensure that we are looking after our team members.</p>
        <h3 style="font-size:12px;margin-top:8px">Aiming for alignment</h3>
        <div class="row" style="gap:18px;margin-bottom:6px"><p>Be frank and rally</p><p>Be wary of agreement!</p></div>
        <div class="row">
          <div style="width:88px">
            <p class="sans" style="font-size:7.5px;font-weight:600;color:#222;line-height:1.15">Make informed decisions</p>
            <p class="sans" style="font-size:6.8px;line-height:1.2">You need the courage to look outside yourself</p>
          </div>
          <div class="placeholder" role="img" aria-label="Diagram of outside self and inside self with reflection, generation and action between two heads" style="flex:1;height:68px;background:linear-gradient(90deg,#ffffff,#f3f0e4 50%,#ffffff);border:1px solid #d8dde1"></div>
        </div>

        <div class="life">
          <div class="life-top">
            <h4>Life balance</h4>
            <p>How many summers do you have left?</p>
          </div>
          <div class="life-bottom">
            <h5>PERSONAL AND STRATEGIC<br>IMPERATIVES</h5>
            <svg width="200" height="118" viewBox="0 0 200 118" aria-label="Life balance wheel">
              <g transform="translate(30,4)" stroke="#fff" stroke-width="1.5">
                <path d="M35.36 35 A40 40 0 0 1 70 15 L70 33 A22 22 0 0 0 50.95 44Z" fill="var(--orange)"/>
                <path d="M70 15 A40 40 0 0 1 104.64 35 L89.05 44 A22 22 0 0 0 70 33Z" fill="var(--sky)"/>
                <path d="M104.64 35 A40 40 0 0 1 104.64 75 L89.05 66 A22 22 0 0 0 89.05 44Z" fill="var(--teal)"/>
                <path d="M104.64 75 A40 40 0 0 1 70 95 L70 77 A22 22 0 0 0 89.05 66Z" fill="var(--blue)"/>
                <path d="M70 95 A40 40 0 0 1 35.36 75 L50.95 66 A22 22 0 0 0 70 77Z" fill="var(--pink)"/>
                <path d="M35.36 75 A40 40 0 0 1 35.36 35 L50.95 44 A22 22 0 0 0 50.95 66Z" fill="var(--coral)"/>
                <circle cx="70" cy="55" r="18" fill="#2c2f33" stroke="#fff"/>
                <text x="70" y="58" fill="#fff" stroke="none" font-size="8" font-weight="700" text-anchor="middle">ME</text>
              </g>
              <g font-size="6.5" fill="#222">
                <text x="74" y="12" text-anchor="middle">Health</text>
                <text x="134" y="12" text-anchor="middle">Career</text>
                <text x="2" y="62">Intrapersonal</text>
                <text x="144" y="62">Relationships</text>
                <text x="70" y="112" text-anchor="middle">Finance</text>
                <text x="128" y="108">Physical</text>
                <text x="128" y="116">Environment</text>
              </g>
            </svg>
          </div>
        </div>
      </div>
    </section>
  </div>
</main>
</body>
</html>
```